Business Card Design

New business card design

Target Market(s)

Residential & Commercial Property Managers

Industry/Entity Type

Plumbing Services

Contact Information for Business Card

Name - Owen Tredgold, title - Director, Phone Number - 0431 862 507, email - owen@rvb-plumbing.com.au, Company ABN - 73 215 904 386,

Font styles to use
Sans Serif

Colors
0054AA
0677BA
7BADD7
CADEEF
E8F1F8

```html
<!DOCTYPE html>
<html lang="en">
<head>
<meta charset="utf-8">
<title>RVB Plumbing Services – Business Card</title>
<link href="https://fonts.googleapis.com/css2?family=Roboto:wght@300;400;700&display=swap" rel="stylesheet">
<style>
  :root {
    --page-bg: #ececec;
    --card-white: #ffffff;
    --card-dark: #1f242b;
    --brand-blue: #00a8e8;
    --edge-blue: #1e9ad6;
    --text-dark: #2a2e33;
    --text-grey: #5a5f66;
  }
  html, body {
    margin: 0;
    padding: 0;
    width: 1200px;
    height: 900px;
    overflow: hidden;
    background: var(--page-bg);
    font-family: "Roboto", Arial, sans-serif;
  }
  .canvas {
    position: relative;
    width: 1200px;
    height: 900px;
  }
  .card {
    position: absolute;
    border-radius: 24px;
    overflow: hidden;
    box-shadow: 0 0 0 3px var(--edge-blue), 0 18px 30px rgba(0,0,0,0.18);
  }

  /* Front */
  .card-front {
    left: 150px;
    top: 170px;
    width: 340px;
    height: 560px;
    background: var(--card-white);
  }
  .front-corner {
    position: absolute;
    left: 0;
    top: 0;
    width: 340px;
    height: 560px;
  }
  .front-brand {
    position: absolute;
    left: 40px;
    top: 44px;
    font-size: 22px;
    font-weight: 300;
    letter-spacing: 3px;
    color: var(--text-dark);
  }
  .contact-block {
    position: absolute;
    left: 40px;
    top: 120px;
  }
  .name-marker {
    position: absolute;
    left: -28px;
    top: 2px;
    width: 16px;
    height: 22px;
    background: var(--brand-blue);
  }
  .person-name {
    margin: 0;
    font-size: 22px;
    font-weight: 700;
    color: var(--brand-blue);
    text-transform: uppercase;
    letter-spacing: 0.3px;
  }
  .person-title {
    margin: 2px 0 14px;
    font-size: 15px;
    color: var(--text-grey);
  }
  .contact-line {
    display: flex;
    align-items: center;
    gap: 6px;
    margin: 0 0 4px;
    font-size: 15px;
    color: var(--text-grey);
  }
  .contact-line .label {
    color: var(--brand-blue);
  }
  .contact-icon {
    width: 12px;
    height: 12px;
    fill: var(--text-grey);
  }

  /* Back */
  .card-back {
    left: 540px;
    top: 280px;
    width: 560px;
    height: 340px;
    background: var(--card-dark);
  }
  .back-pattern {
    position: absolute;
    inset: 0;
    background: linear-gradient(135deg, #242a31 0%, #1d2228 100%);
  }
  .back-brand {
    position: absolute;
    inset: 0;
    display: flex;
    align-items: center;
    justify-content: center;
    font-size: 30px;
    font-weight: 300;
    letter-spacing: 4px;
    color: var(--card-white);
  }
</style>
</head>
<body>
<main class="canvas">

  <section class="card card-front" aria-label="Business card front">
    <svg class="front-corner" viewBox="0 0 340 560" aria-hidden="true">
      <path d="M340 230 C 320 380, 220 480, 80 560 L340 560 Z" fill="#1f242b"/>
      <path d="M332 250 C 300 390, 210 470, 100 545" fill="none" stroke="#ffffff" stroke-width="6"/>
      <path d="M318 252 C 280 380, 200 460, 110 520 L 150 560 L 90 560 C 210 470, 300 390, 322 250 Z" fill="#00a8e8"/>
    </svg>

    <div class="front-brand">rvb plumbing services</div>

    <div class="contact-block">
      <span class="name-marker"></span>
      <h1 class="person-name">Owen Tredgold</h1>
      <p class="person-title">Director</p>
      <p class="contact-line"><span class="label">ABN:</span> 73 215 904 386</p>
      <p class="contact-line">
        <svg class="contact-icon" viewBox="0 0 12 12" aria-hidden="true"><path d="M2 1h2.5l1 3-1.5 1a7 7 0 0 0 3 3l1-1.5 3 1V10a1 1 0 0 1-1 1A10 10 0 0 1 1 2a1 1 0 0 1 1-1z"/></svg>
        0431 862 507
      </p>
      <p class="contact-line">
        <svg class="contact-icon" viewBox="0 0 12 12" aria-hidden="true"><path d="M1 2.5h10v7H1z M1 2.5l5 4 5-4" fill="none" stroke="#5a5f66" stroke-width="1.2"/></svg>
        owen@rvb-plumbing.com.au
      </p>
    </div>
  </section>

  <section class="card card-back" aria-label="Business card back">
    <div class="back-pattern" role="img" aria-label="Faint repeating water drop pattern on dark background"></div>
    <div class="back-brand">rvb plumbing services</div>
  </section>

</main>
</body>
</html>
```